Layout for new page on existing website

We have an existing website (www.brightloomworks.org) and need a new page designing to promote a new product.
The new page needs to be consistent with the existing website look and feel (www.brightloomworks.org) but current persistent elements on the standard page design can be moved/removed from the page to accommodate a new layout necessary for getting all the content laid out in a logical user friendly way.
The content required for the page is attached along with a wireframe mock up that may help understand the expectation, however the wireframe was just created to help me work out what was needed on the page and the layout can be different. A key element is the quality of the design of each of the artifacts (e.g. the panel the embedded video needs to go in, icons etc) and a clear display of the information.
Updates
The website that the new page needs to fit into is www.brightloomworks.org, i will also added the company logo to the brief.
Our Corporate Colours
- Green: #A2FF00
- Cream: #FFFF99
- Yellow: #FFE900
- Grey: #534741
Industry/Entity Type
Product
Look and feel
Each slider illustrates characteristics of the customer's brand and the style your logo design should communicate.

```html
<!DOCTYPE html>
<html lang="en">
<head>
<meta charset="utf-8">
<title>Brightloom Works – Course Management &amp; Booking</title>
<link href="https://fonts.googleapis.com/css2?family=Cabin:wght@400;600;700&display=swap" rel="stylesheet">
<style>
:root{
  --green:#a2ff00;
  --lime:#c9ff3a;
  --lime-light:#e4ff45;
  --cream:#ffff99;
  --yellow:#ffe900;
  --grey:#534741;
  --grey-dark:#3e3531;
  --panel:#463d37;
  --panel-band:#5a504a;
  --text:#e8e2dc;
  --nav-text:#f3ece2;
  --hero-bg:#ecebe9;
}
*{box-sizing:border-box;margin:0;padding:0}
html,body{width:1200px;height:903px;overflow:hidden}
body{background:var(--grey);font-family:"Cabin",sans-serif;position:relative;color:var(--text)}
.site-header{position:absolute;left:0;top:0;width:1200px;height:94px;background:var(--grey-dark)}
.brand{position:absolute;left:0;top:42px;width:1200px;text-align:center;font-weight:700;font-size:25px;letter-spacing:1px;color:#fff}
.brand-dot{display:inline-block;width:16px;height:16px;border-radius:50%;background:var(--green);margin:0 8px 0 0;vertical-align:1px}

.main-nav{position:absolute;left:168px;top:100px;width:100px}
.nav-item{position:absolute;left:0;width:100px;text-align:center;font-size:10px;font-weight:700;color:var(--nav-text)}
.nav-item svg{display:block;margin:0 auto 6px;filter:drop-shadow(0 0 4px rgba(255,233,0,.6))}
.nav-item::after{content:"";display:block;width:70px;height:6px;margin:6px auto 0;border-radius:50%;background:radial-gradient(rgba(0,0,0,.35),transparent 70%)}

.content{position:absolute;left:257px;top:93px;width:534px;height:810px;background:#5b514b}
.hero{position:absolute;left:0;top:0;width:534px;height:149px;background:var(--hero-bg)}
.hero-photo{position:absolute;left:205px;top:0;width:329px;height:127px;background:linear-gradient(90deg,#d8d2cc,#b9aba0 40%,#9a8f8a 70%,#c8c4c0)}
.hero-title{position:absolute;left:22px;top:34px;font-size:20px;font-weight:700;color:#4b4039;line-height:24px}
.hero-band{position:absolute;left:0;top:127px;width:534px;height:22px;background:var(--yellow);font-size:13px;font-weight:600;color:#3e3531;padding:4px 0 0 22px}

.info-panel{position:absolute;left:17px;top:147px;width:517px;height:609px;background:var(--panel)}
.section-title{position:absolute;left:10px;font-size:14px;font-weight:600;color:var(--green)}
.band{position:absolute;left:0;top:366px;width:517px;height:26px;background:var(--panel-band)}
.feature{position:absolute;width:242px;font-size:8.4px;line-height:18.5px;color:var(--text)}
.feature .icon{float:left;width:30px;height:30px;margin:2px 5px 0 -2px}
.feature b,.benefits b{color:var(--yellow);font-weight:600}
.benefits{position:absolute;left:10px;top:396px;width:496px;font-size:8.4px;line-height:18.4px}

.footer{position:absolute;left:0;top:776px;width:534px;font-size:8.5px;color:#a89a8e;text-align:center;letter-spacing:.3px}
.footer-mark{position:absolute;left:452px;top:772px;width:18px;height:18px;border-radius:50%;border:2px solid #d8c470}

.sidebar{position:absolute;left:791px;top:93px;width:204px;height:810px;background:linear-gradient(160deg,var(--lime) 0%,var(--lime-light) 60%,#dcff3c 100%);overflow:hidden}
.sidebar-curve{position:absolute;border-radius:50%;background:rgba(255,255,150,.25)}
.video{position:absolute;left:17px;top:58px;width:172px;height:133px;background:#c9c3b3;border:2px solid #e7e4d8}
.video-screen{position:absolute;left:2px;top:2px;width:164px;height:115px;background:#000}
.video-bar{position:absolute;left:2px;top:119px;width:164px;height:9px;background:#dcd8cc}
.quote{position:absolute;left:19px;top:227px;width:166px;height:277px;background:rgba(255,255,190,.45);padding:8px 9px 0 9px;font-size:11px;line-height:28.2px;color:#3e3531;text-align:justify}
.quote .mark{font-size:42px;font-weight:700;line-height:0;vertical-align:-13px;color:#3e3531;letter-spacing:-2px}
.quote-by{font-size:9px;line-height:14px;margin-top:0;text-align:left;white-space:nowrap}
.contact-title{position:absolute;left:15px;top:561px;font-size:14.5px;font-weight:600;color:#4b4039}
.contact-sub{position:absolute;left:15px;top:579px;font-size:11px;color:#4b4039}
.field{position:absolute;left:15px;width:176px;font-size:10.5px;color:#4b4039}
.field span{display:inline-block;width:46px}
.field i{position:absolute;left:47px;top:-2px;width:132px;height:16px;background:#fff;border:1px solid #a9a391;border-right-width:2px;border-bottom-width:2px}
</style>
</head>
<body>
<header class="site-header">
  <div class="brand"><span class="brand-dot"></span>BRIGHTLOOM WORKS</div>
</header>

<nav class="main-nav">
  <div class="nav-item" style="top:14px">
    <svg width="34" height="32" viewBox="0 0 34 32" fill="none" stroke="#ffe900" stroke-width="2.5"><path d="M3 16 17 4l14 12"/><path d="M7 14v14h8v-8h4v8h8V14"/></svg>Home</div>
  <div class="nav-item" style="top:124px">
    <svg width="34" height="32" viewBox="0 0 34 32" fill="none" stroke="#ffe900" stroke-width="2.5" stroke-linejoin="round"><path d="M17 2l4.3 9.3 10 1-7.5 6.8 2.2 10L17 24l-9 5.1 2.2-10L2.7 12.3l10-1z"/></svg>About Us</div>
  <div class="nav-item" style="top:202px">
    <svg width="34" height="32" viewBox="0 0 34 32" fill="none" stroke="#ffe900" stroke-width="2.5" stroke-linejoin="round"><path d="M4 28 30 3 22 29l-6-9-9-2z"/><path d="M16 20 30 3"/></svg>Our Services</div>
  <div class="nav-item" style="top:280px">
    <svg width="34" height="32" viewBox="0 0 34 32" fill="none" stroke="#ffe900" stroke-width="2.5"><circle cx="17" cy="16" r="13"/><rect x="11" y="11" width="12" height="10" rx="1"/></svg>Portfolio</div>
  <div class="nav-item" style="top:358px">
    <svg width="34" height="32" viewBox="0 0 34 32" fill="none" stroke="#ffe900" stroke-width="2.5" stroke-linejoin="round"><path d="M4 14c0-6 6-10 13-10s13 4 13 10-6 10-13 10c-2 0-3 0-5-1l-7 5 2-6c-2-2-3-5-3-8z"/><path d="M11 12h12M11 17h8"/></svg>Testimonials</div>
  <div class="nav-item" style="top:436px">
    <svg width="34" height="32" viewBox="0 0 34 32" fill="none" stroke="#ffe900" stroke-width="2.5" stroke-linejoin="round"><path d="M3 12c0-5 6-8 14-8s14 3 14 8l-6 2-1-4c-4-1-10-1-14 0l-1 4z"/><path d="M8 16h18l3 12H5z"/><circle cx="17" cy="22" r="3"/></svg>Contact Us</div>
</nav>

<main class="content">
  <section class="hero">
    <div class="hero-photo" role="img" aria-label="Photo of three smiling business people in office attire"></div>
    <h1 class="hero-title">Course Management<br>&amp; Booking Simplified</h1>
    <div class="hero-band">Built with your business in mind.</div>
  </section>

  <section class="info-panel">
    <h2 class="section-title" style="top:28px">Key Features:</h2>

    <div class="feature" style="left:9px;top:54px">
      <svg class="icon" viewBox="0 0 30 30"><circle cx="15" cy="15" r="14" fill="#2a2420" stroke="#a2ff00" stroke-width="1.5"/><circle cx="15" cy="15" r="9" fill="none" stroke="#fff" stroke-width="2"/><path d="M15 9v6h4" stroke="#fff" stroke-width="2" fill="none"/></svg>
      <b>Available and easy to use 24/7</b> - By allowing booking and payment at any time of the day, your attendees will be more likely to commit to your event and with no account setup or password required and no paper forms to fill in and post, booking onto and paying for your courses is easy.</div>

    <div class="feature" style="left:265px;top:54px">
      <svg class="icon" viewBox="0 0 30 30"><circle cx="15" cy="15" r="14" fill="#2a2420" stroke="#a2ff00" stroke-width="1.5"/><rect x="10" y="8" width="10" height="14" fill="none" stroke="#fff" stroke-width="1.8"/><path d="M12 12h6M12 15h6M12 18h6" stroke="#fff" stroke-width="1.2"/></svg>
      <b>Online Course promotion</b> - List your upcoming courses in a clear and simple way so people can easily find and select the course that suits them.</div>

    <div class="feature" style="left:9px;top:157px">
      <svg class="icon" viewBox="0 0 30 30"><circle cx="15" cy="15" r="14" fill="#2a2420" stroke="#a2ff00" stroke-width="1.5"/><rect x="8" y="9" width="14" height="10" fill="none" stroke="#fff" stroke-width="1.8"/><path d="M12 22h6M15 19v3" stroke="#fff" stroke-width="1.8"/></svg>
      <b>Online &amp; Offline Payments</b> - Take payments online, whilst having the flexibility of managing and adding offline payments.</div>

    <div class="feature" style="left:265px;top:157px">
      <svg class="icon" viewBox="0 0 30 30"><circle cx="15" cy="15" r="14" fill="#2a2420" stroke="#a2ff00" stroke-width="1.5"/><rect x="8" y="10" width="14" height="10" fill="none" stroke="#fff" stroke-width="1.8"/><path d="M8 10l7 6 7-6" stroke="#fff" stroke-width="1.5" fill="none"/></svg>
      <b>Built in email system</b> - Enable quick and easy communication with upcoming course candidates and promotion of additional courses to past candidates.</div>

    <div class="feature" style="left:9px;top:234px">
      <svg class="icon" viewBox="0 0 30 30"><circle cx="15" cy="15" r="14" fill="#2a2420" stroke="#a2ff00" stroke-width="1.5"/><path d="M10 21l2-5 8-8 3 3-8 8z" fill="none" stroke="#fff" stroke-width="1.8"/></svg>
      <b>Customisable look and feel</b> - All elements of the booking systems design will fit in with your existing websites style.</div>

    <div class="feature" style="left:265px;top:234px">
      <svg class="icon" viewBox="0 0 30 30"><circle cx="15" cy="15" r="14" fill="#2a2420" stroke="#a2ff00" stroke-width="1.5"/><path d="M11 14v-3a4 4 0 0 1 8 0v3" fill="none" stroke="#fff" stroke-width="1.8"/><rect x="9" y="14" width="12" height="9" rx="1" fill="#fff"/></svg>
      <b>Live course place availability</b> - By defining minimum and maximum candidates permitted on a course its easy to prevent overbooking and also prevent courses running that don't have enough candidates.</div>

    <div class="feature" style="left:9px;top:309px">
      <svg class="icon" viewBox="0 0 30 30"><circle cx="15" cy="15" r="14" fill="#2a2420" stroke="#a2ff00" stroke-width="1.5"/><path d="M12 19c0-3-3-4-3-8a6 6 0 0 1 12 0c0 4-3 5-3 8z" fill="none" stroke="#fff" stroke-width="1.8"/><path d="M12 22h6" stroke="#fff" stroke-width="1.8"/></svg>
      <b>Venue database management</b> - Easily add, edit and remove venues from which you operate your courses from.</div>

    <div class="band"></div>
    <h2 class="section-title" style="top:370px">Key Benefits:</h2>
    <div class="benefits">
      <b>Live Availability</b> - Availability on course place availability to prevent overbooking. Customers can search for Courses and Book Online with immediate confirmation.<br>
      <b>Automated confirmation emails</b> - Be available for business 24/7 and take orders anytime! Customers can book when it's most convenient for them – be it early morning, late evening or weekend. No fielding phone calls, no wading through paper registrations. Attendees book on your website, there and then.<br>
      <b>No more trips to the bank</b>- Take immediate and secure payments online. Automated confirmation emails so reducing the time need communicating with candidates.<br>
      <b>Boost course bookings and reduce administrative time and costs</b> - CourseDesk is Web based meaning you can access your course information from anywhere at any time. System is very intuitive and easy to use.<br>
      <b>Lighten your workload</b> - Upload and manage offline bookings through the admin dashboard. Keep your attendees organized all the way up to the course date and beyond.
    </div>
  </section>

  <footer class="footer">| ©2010 Brightloom Works. All Rights Reserved | Disclaimer |</footer>
  <div class="footer-mark"></div>
</main>

<aside class="sidebar">
  <div class="sidebar-curve" style="left:60px;top:420px;width:320px;height:320px"></div>
  <div class="sidebar-curve" style="left:-120px;top:-60px;width:260px;height:200px"></div>
  <div class="video">
    <div class="video-screen">
      <svg width="164" height="115" viewBox="0 0 164 115"><path d="M80 52l10 6-10 6z" fill="#fff"/></svg>
    </div>
    <div class="video-bar">
      <svg width="164" height="9" viewBox="0 0 164 9"><path d="M3 2l4 2.5-4 2.5z" fill="#333"/><rect x="30" y="3.5" width="90" height="2" fill="#8a857a"/><path d="M147 2l5 5M152 2l-5 5" stroke="#333"/><path d="M156 4.5l5-3v6z" fill="#333"/></svg>
    </div>
  </div>
  <blockquote class="quote"><span class="mark">“</span>A convenient tool that was simple to integrate into our website. It has allowed both the business and our customers an easy way to book courses. In life sometimes simple is good and this is a great example!<span class="mark">”</span>
    <div class="quote-by"><b>- Dana Whitlow,</b> Director @ TrainPath<br>www.trainpath.org</div>
  </blockquote>
  <h3 class="contact-title">Contact Us Now</h3>
  <p class="contact-sub">for a free no obligation quote.</p>
  <div class="field" style="top:604px"><span>Name</span><i></i></div>
  <div class="field" style="top:638px"><span>Company</span><i></i></div>
  <div class="field" style="top:670px"><span>Email</span><i></i></div>
  <div class="field" style="top:702px"><span>Telephone</span><i></i></div>
</aside>
</body>
</html>
```